Brand new letterhead, business card, email signature etc.

We are a financial company in London, UK. Our website is www.quorvane.com. We're wanting a complete remodel of the company colours, letter head, business cards, email signatures, etc. Looking to keep the same font for the company name. I have upload a colour palette that we want to work with. We're looking for company letterhead for outgoing letters/ correspondence, letterhead for internal documentation, email signatures, e-letters. etc. Ultimately we will redesign the entire website also. It is important that our clients get a strong, secure, warm, trustworthy, solid feeling and first impression.
Updates

Designs look the same

Target Market(s)

Institutional investors, (ultra) high net worth individuals

Industry/Entity Type

Finance, Invesments banking.

Font styles to use
Other font styles liked:
• Current font is "Champagne & Limousines"

Requirements
Must have
• Must use the colours provided on the PDF uploaded to the portal. The purple = main colour. The red = accent colour.
Nice to have
• Nice to use same font as now for the company name "Marlowin". Font is "Champagne & Limousines". Nice to have some reference to the old logo flower, but only subtle.
Should not have
• Do not use the colour red from our website. Use the colours provided on the colour palette PDF that I uploaded in the portal.

```html
<!DOCTYPE html>
<html lang="en">
<head>
<meta charset="utf-8">
<title>Marlowin Letterhead</title>
<link rel="stylesheet" href="https://fonts.googleapis.com/css2?family=Jost:wght@300;400&display=swap">
<style>
  :root {
    --backdrop: #e8e7e4;
    --paper: #fbfbfa;
    --band-top: #e84d1f;
    --band-mid: #8a1c1a;
    --band-bottom: #2a0019;
    --ink: #2b2b2b;
    --ink-soft: #6e6e6e;
    --accent: #e0461c;
    --rule: #9a9a9a;
  }
  * { margin: 0; padding: 0; box-sizing: border-box; }
  html, body {
    width: 1200px; height: 900px; overflow: hidden;
    background: var(--backdrop);
    font-family: "Jost", sans-serif;
    font-weight: 300;
  }
  .letterhead {
    position: absolute; left: 296px; top: 20px;
    width: 608px; height: 860px;
    background: var(--paper);
    box-shadow: 0 2px 10px rgba(0,0,0,0.12);
  }
  .side-band {
    position: absolute; left: 0; top: 0; bottom: 0; width: 54px;
    background: linear-gradient(to bottom, var(--band-top) 0%, var(--band-mid) 45%, var(--band-bottom) 90%);
  }
  .brand {
    position: absolute; left: 38px; top: 43px; height: 54px;
    display: flex; align-items: center; gap: 14px;
  }
  .brand-square {
    width: 54px; height: 54px;
    border: 1px solid var(--ink);
    background: var(--paper);
  }
  .brand-name {
    font-size: 30px; font-weight: 300; letter-spacing: 0.16em;
    color: var(--ink); text-transform: uppercase; line-height: 1;
  }
  .contact-block {
    position: absolute; top: 56px; left: 346px;
    display: flex; font-size: 8.6px; line-height: 11px; color: var(--ink-soft);
  }
  .address { padding-right: 10px; border-right: 1px solid var(--rule); }
  .channels { padding-left: 10px; }
  .channel { display: flex; align-items: center; gap: 5px; }
  .channel svg { width: 6px; height: 6px; flex: none; }
  .letter-date {
    position: absolute; right: 41px; top: 230px;
    font-size: 11px; color: var(--ink-soft);
  }
  .letter-body {
    position: absolute; left: 130px; width: 437px; top: 256px;
    font-size: 11.1px; line-height: 17.3px; color: var(--ink-soft);
  }
  .salutation { margin-bottom: 11px; }
  .letter-body p.para { text-align: justify; margin-bottom: 22px; }
  .letter-body p.para:nth-of-type(3) { margin-bottom: 26px; }
  .signature {
    position: absolute; left: 130px; top: 622px; width: 93px; height: 60px;
    background: linear-gradient(to right, rgba(40,40,40,0.16), rgba(40,40,40,0.04));
  }
</style>
</head>
<body>
  <main class="letterhead">
    <div class="side-band"></div>

    <header>
      <div class="brand">
        <div class="brand-square"></div>
        <span class="brand-name">Marlowin</span>
      </div>

      <div class="contact-block">
        <div class="address">
          <div>Suite 42/1180</div>
          <div>Ashmere Lane</div>
          <div>Holbrook VIC 3120</div>
        </div>
        <div class="channels">
          <div class="channel">
            <svg viewBox="0 0 10 10"><path d="M2 1 L4 1 L4.6 3 L3.4 3.8 Q4.6 6 6.2 6.6 L7 5.4 L9 6 L9 8 Q8.6 9 7.6 9 Q1 8 1 2.4 Q1 1 2 1 Z" fill="var(--accent)"/></svg>
            <span>1840 36 72 18</span>
          </div>
          <div class="channel">
            <svg viewBox="0 0 10 10"><rect x="0.5" y="2" width="9" height="6.4" fill="var(--accent)"/><path d="M0.8 2.3 L5 5.6 L9.2 2.3" fill="none" stroke="var(--paper)" stroke-width="1"/></svg>
            <span>contact@quorvane.com</span>
          </div>
          <div class="channel">
            <svg viewBox="0 0 10 10"><circle cx="5" cy="5" r="4.2" fill="none" stroke="var(--accent)" stroke-width="1.2"/><ellipse cx="5" cy="5" rx="1.8" ry="4.2" fill="none" stroke="var(--accent)" stroke-width="0.9"/><line x1="0.8" y1="5" x2="9.2" y2="5" stroke="var(--accent)" stroke-width="0.9"/></svg>
            <span>quorvane.com</span>
          </div>
        </div>
      </div>
    </header>

    <div class="letter-date">Dated: February 15, 2023</div>

    <section class="letter-body">
      <p class="salutation">Dear Sir,</p>
      <p class="para">Lorem Ipsum is simply dummy text of the printing and typesetting industry. Lorem Ipsum has been the industry's standard dummy text ever since the 1500s, when an unknown printer took a galley of type and scrambled it to make a type specimen book. It has survived not only five centuries, but also the leap into electronic typesetting, remaining essentially unchanged. It was popularised in the 1960s with the release of Pressline sheets containing Lorem Ipsum passages, and more recently</p>
      <p class="para">It is a long established fact that a reader will be distracted by the readable content of a page when looking at its layout. The point of using Lorem Ipsum is that it has a more-or-less normal distribution of letters, as opposed to using 'Content here, content here', making it look like readable English. Many desktop publishing packages and web page editors now use Lorem Ipsum as their default model text, and a search for 'lorem ipsum' will uncover many web sites still in their infancy. Various versions have</p>
      <p class="para">The standard chunk of Lorem Ipsum used since the 1500s is reproduced below for those interested. Sections 1.10.32 and 1.10.33 from "de Finibus Bonorum et Malorum" by Varennius are also reproduced in their exact original form, accompanied by English versions from the 1914 translation by J. Ellory.</p>
    </section>

    <div class="signature" role="img" aria-label="Handwritten signature of the sender"></div>
  </main>
</body>
</html>
```